Want a package created for a new protein bar

We would like a new package created for a new protein bar project The name of the bar will be VOLMBite a real food protein bar, we would like a ‘window’ on the package of bar like Brave Meadow bar below in images.

VOLMBite
‘Super Food Bar’
14g of Whey Protein
The package film size is the following 12cm width x 15cm Length,
Flavor Peanut Chocolate Chip, additional information will be attached shortly like nutrition facts,

Target Market(s)

fitness market, bodybuilders, athletes, everyday people

Industry/Entity Type

Health Product

Logo Text

VOLMBite

Font styles to use
Serif
Sans Serif
Decorative

Requirements
Must have
• Package window

```html
<!DOCTYPE html>
<html lang="en">
<head>
<meta charset="utf-8">
<title>VOLMBite Super Food Bar – Wrapper</title>
<link href="https://fonts.googleapis.com/css2?family=Archivo+Black&family=Roboto+Slab:wght@700&family=Roboto:ital,wght@0,700;1,900&display=swap" rel="stylesheet">
<style>
  :root {
    --bg: #efefef;
    --yellow: #f6d313;
    --yellow-deep: #e9bf00;
    --yellow-light: #fde55a;
    --black: #141414;
    --ink: #111111;
    --white: #ffffff;
    --oat: #e8d3bd;
    --berry: #d98a78;
  }
  * { margin: 0; padding: 0; box-sizing: border-box; }
  html, body { width: 1200px; height: 750px; overflow: hidden; background: var(--bg); }
  .canvas { position: relative; width: 1200px; height: 750px; }
  .wrapper-art { position: absolute; inset: 0; }
  .brand-name {
    position: absolute; left: 333px; top: 270px;
    font-family: "Archivo Black", sans-serif; font-size: 50px; line-height: 1;
    color: var(--ink); letter-spacing: -1px;
  }
  .tagline {
    position: absolute; left: 335px; top: 348px;
    font-family: "Roboto Slab", serif; font-weight: 700; font-size: 17px;
    letter-spacing: 3.2px; color: var(--ink);
  }
  .flavor-label {
    position: absolute; left: 333px; top: 393px; width: 238px; height: 43px;
    background: var(--black); color: var(--yellow);
    font-family: "Roboto", sans-serif; font-style: italic; font-weight: 900;
    font-size: 14px; line-height: 16px; padding: 5px 10px; letter-spacing: 0.3px;
  }
  .claim {
    position: absolute; left: 333px; top: 442px;
    font-family: "Roboto", sans-serif; font-weight: 700; font-size: 11.5px; color: var(--ink);
  }
  .fact { position: absolute; left: 800px; width: 96px; text-align: right; color: var(--yellow); font-family: "Roboto", sans-serif; }
  .fact-value { font-family: "Archivo Black", sans-serif; font-size: 25px; line-height: 1; }
  .fact-label { font-weight: 700; font-size: 8px; letter-spacing: 0.4px; margin-top: 2px; }
  .fact-sugar { top: 306px; }
  .fact-protein { top: 352px; }
  .net-weight {
    position: absolute; left: 800px; top: 418px; width: 96px; text-align: right;
    font-family: "Roboto", sans-serif; font-weight: 700; font-size: 8.5px; line-height: 11px; color: var(--white);
  }
</style>
</head>
<body>
<main class="canvas">
  <svg class="wrapper-art" viewBox="0 0 1200 750" width="1200" height="750" aria-hidden="false">
    <defs>
      <linearGradient id="film-yellow" x1="0" y1="0" x2="0" y2="1">
        <stop offset="0" stop-color="var(--yellow-deep)"/>
        <stop offset="0.2" stop-color="var(--yellow-light)"/>
        <stop offset="0.55" stop-color="var(--yellow)"/>
        <stop offset="1" stop-color="var(--yellow-deep)"/>
      </linearGradient>
      <linearGradient id="window-fill" x1="0" y1="0" x2="1" y2="1">
        <stop offset="0" stop-color="var(--oat)"/>
        <stop offset="0.5" stop-color="var(--berry)"/>
        <stop offset="1" stop-color="var(--oat)"/>
      </linearGradient>
      <pattern id="crimp-ridges" width="6" height="10" patternUnits="userSpaceOnUse">
        <rect width="3" height="10" fill="rgba(0,0,0,0.12)"/>
      </pattern>
      <filter id="soft-shadow" x="-10%" y="-20%" width="120%" height="150%">
        <feDropShadow dx="0" dy="8" stdDeviation="7" flood-color="#000" flood-opacity="0.22"/>
      </filter>
    </defs>

    <g class="wrapper" filter="url(#soft-shadow)">
      <path class="crimp-left" fill="url(#film-yellow)"
        d="M300 258 H252 l-4 4 4 4 l-4 4 4 4 l-4 4 4 4 l-4 4 4 4 l-4 4 4 4 l-4 4 4 4 l-4 4 4 4 l-4 4 4 4 l-4 4 4 4 l-4 4 4 4 l-4 4 4 4 l-4 4 4 4 l-4 4 4 4 l-4 4 4 4 l-4 4 4 4 l-4 4 4 4 l-4 4 4 4 l-4 4 4 4 l-4 4 4 4 l-4 4 4 4 l-4 4 4 4 l-4 4 4 4 l-4 4 4 4 l-4 4 4 4 l-4 4 4 4 H300 Z"/>
      <rect x="252" y="258" width="48" height="200" fill="url(#crimp-ridges)"/>
      <rect class="wrapper-body" x="300" y="262" width="310" height="192" fill="url(#film-yellow)"/>
      <rect class="bar-window" x="608" y="262" width="190" height="192" fill="url(#window-fill)"
        role="img" aria-label="Window showing the peanut chocolate chip bar inside"/>
      <rect class="info-panel" x="796" y="262" width="104" height="192" fill="var(--black)"/>
      <path class="crimp-right" fill="var(--black)"
        d="M900 258 H958 l4 4 -4 4 l4 4 -4 4 l4 4 -4 4 l4 4 -4 4 l4 4 -4 4 l4 4 -4 4 l4 4 -4 4 l4 4 -4 4 l4 4 -4 4 l4 4 -4 4 l4 4 -4 4 l4 4 -4 4 l4 4 -4 4 l4 4 -4 4 l4 4 -4 4 l4 4 -4 4 l4 4 -4 4 l4 4 -4 4 l4 4 -4 4 l4 4 -4 4 l4 4 -4 4 l4 4 -4 4 l4 4 -4 4 l4 4 -4 4 l4 4 -4 4 H900 Z"/>
      <rect x="904" y="258" width="54" height="200" fill="url(#crimp-ridges)" opacity="0.6"/>
      <line x1="808" y1="341" x2="896" y2="341" stroke="var(--yellow)" stroke-width="0.8"/>
      <line x1="808" y1="388" x2="896" y2="388" stroke="var(--yellow)" stroke-width="0.8"/>
      <line x1="808" y1="411" x2="896" y2="411" stroke="var(--yellow)" stroke-width="0.8"/>
    </g>
  </svg>

  <div class="brand-name">VOLMBite</div>
  <div class="tagline">SUPER FOOD BAR</div>
  <div class="flavor-label">PEANUT CHOCOLATE CHIP<br>FLAVOR</div>
  <div class="claim">NO ARTIFICIAL FLAVORS OR COLORS</div>

  <div class="fact fact-sugar"><div class="fact-value">2g</div><div class="fact-label">SUGAR</div></div>
  <div class="fact fact-protein"><div class="fact-value">14g</div><div class="fact-label">WHEY PROTEIN</div></div>
  <div class="net-weight">NET WT.<br>2.12 oz (60g)</div>
</main>
</body>
</html>
```